letter head for a construction company

Company Name: Zaviro Construction Limited

Address: Kilele Street, Tengeru Shores, Dar es salaam, Tanzania

Phone: 0754382916

email : info@zaviroconstruction.example

website : www.zaviroconstruction.example

```html
<!DOCTYPE html>
<html lang="en">
<head>
<meta charset="utf-8">
<title>Zaviro Construction Limited – Letterhead</title>
<link rel="stylesheet" href="https://fonts.googleapis.com/css2?family=Arimo:wght@400;700&family=Questrial&display=swap">
<style>
  :root {
    --backdrop: #e2e2e2;
    --paper: #ffffff;
    --charcoal: #444545;
    --orange: #ec7400;
    --body-text: #555555;
    --heading-text: #4a4a4a;
    --footer-text: #7a7a7a;
    --rule: #9a9a9a;
    --signature-fill: #ededed;
  }
  * { margin: 0; padding: 0; box-sizing: border-box; }
  html, body {
    width: 978px; height: 1200px; overflow: hidden;
    background: var(--backdrop);
  }
  .letterhead {
    position: absolute; left: 138px; top: 104px;
    width: 703px; height: 993px;
    background: var(--paper);
    box-shadow: 2px 2px 4px rgba(0,0,0,0.35);
    overflow: hidden;
  }
  .header-swoosh { position: absolute; left: 0; top: 0; width: 703px; height: 100px; }
  .brand {
    position: absolute; left: 0; top: 60px; width: 100%;
    text-align: center; color: var(--charcoal);
    font-family: "Questrial", sans-serif; font-weight: 400;
  }
  .brand-name { font-size: 42px; line-height: 36px; letter-spacing: 2px; }
  .brand-sub { font-size: 14px; letter-spacing: 4.6px; margin-top: 4px; }
  .greeting {
    position: absolute; left: 65px; top: 305px;
    font-family: "Questrial", sans-serif; font-size: 17px; font-weight: 400;
    color: var(--heading-text); -webkit-text-stroke: 0.4px var(--heading-text);
  }
  .letter-body {
    position: absolute; left: 63px; top: 352px; width: 576px;
    font-family: "Arimo", sans-serif; font-size: 12.1px; line-height: 14.5px;
    color: var(--body-text);
  }
  .letter-body p { margin-bottom: 12px; }
  .closing {
    position: absolute; left: 64px; top: 652px;
    font-family: "Questrial", sans-serif; font-size: 10px;
    color: var(--heading-text); -webkit-text-stroke: 0.3px var(--heading-text);
  }
  .signature {
    position: absolute; left: 63px; top: 690px; width: 117px; height: 34px;
    background: var(--signature-fill);
  }
  .footer {
    position: absolute; left: 0; top: 933px; width: 100%;
    font-family: "Arimo", sans-serif; color: var(--footer-text);
  }
  .footer-address { text-align: center; font-size: 11px; }
  .footer-rule { margin: 4px 0 0 130px; width: 443px; height: 1px; background: var(--rule); }
  .footer-contacts {
    display: flex; justify-content: center; align-items: center; gap: 9px;
    margin-top: 5px; font-size: 11px;
  }
  .contact-item { display: flex; align-items: center; gap: 6px; }
  .contact-icon { width: 9px; height: 9px; }
</style>
</head>
<body>
  <main class="letterhead">
    <svg class="header-swoosh" viewBox="0 0 703 100" aria-hidden="true">
      <path d="M0,0 H703 V39 Q400,-22 0,61 Z" fill="var(--charcoal)"/>
      <path d="M0,64 Q360,-6 589,29 Q360,10 0,88 Z" fill="var(--orange)"/>
    </svg>

    <header class="brand">
      <div class="brand-name">ZAVIRO</div>
      <div class="brand-sub">CONSTRUCTION LIMITED</div>
    </header>

    <h1 class="greeting">Dear Mr. Halden,</h1>

    <section class="letter-body">
      <p>Lorem ipsum dolor sit amet, consectetuer adipiscing elit, sed diam nonmmy nibh euismod tincidunt ut laor eet dolore magna aliquam erat volutpat. Ut wisi enim ad minim veniam, quis nostrud exerci tationmcorper suscipit lobortis nisl ut aliquip ex ea commodo consequat. Duis autem vel eum iriure dolor in hendrerit in vulputate velit esse molestie consequat, vel illum dolore eu feugiat</p>
      <p>Rorem ipsum dolor sit amet, consectetuer adipiscing elit, sed diam nonmmy nibh euismod tincidunt ut laor eet dolore magna aliquam erat volutpat. Ut wisi enim ad minim veniam, quis nostrud exerci tationmcorper suscipit lobortis nisl ut aliquip ex ea commodo consequat. Duis autem vel eum iriure dolor in hendrerit in vulputate velit esse molest</p>
      <p>Dorem ipsum dolor sit amet, consectetuer adipiscing elit, sed diam nonmmy nibh euismod tincidunt ut laor eet dolore magna aliquam erat volutpat. Ut wisi enim ad minim veniam, quis nostrud exerci tationmcorper suscipit lobortis nisl ut aliquip ex ea commodo consequat. Duis autem vel eum iriure dolor in hendrerit in suscipit lobortis nisl ut aliquip ex ea commodo consequat. Duis autem vel eum iriure dolor in hendrerit in vulputate velit esse molestie consequat, vel illum</p>
      <p>Sorem ipsum dolor sit amet, consectetuer adipiscing elit, sed diam nonmmy nibh euismod tincidunt ut laor eet dolore magna aliquam erat volutpat. Ut wisi enim ad minim veniam, quis nostrud exerci tationmcorper suscipit lobortis nisl ut aliquip ex ea commodo consequat. Duis autem vel eum iriure dolor in</p>
    </section>

    <div class="closing">Sincerely,</div>
    <div class="signature" role="img" aria-label="Handwritten signature of the sender"></div>

    <footer class="footer">
      <div class="footer-address">Kilele Street, Tengeru Shores, Dar es salaam, Tanzania</div>
      <div class="footer-rule"></div>
      <div class="footer-contacts">
        <span class="contact-item">
          <svg class="contact-icon" viewBox="0 0 10 10" aria-hidden="true"><path d="M2,0.5 L3.8,2.6 L2.8,3.6 Q3.8,5.8 6.2,7 L7.3,6 L9.5,7.8 L8.2,9.5 Q1.5,8.5 0.5,1.8 Z" fill="var(--orange)"/></svg>
          0754382916
        </span>
        <span class="contact-item">
          <svg class="contact-icon" viewBox="0 0 10 10" aria-hidden="true"><rect x="0" y="2" width="10" height="6.5" fill="var(--orange)"/><path d="M0.3,2.3 L5,5.6 L9.7,2.3" stroke="#fff" stroke-width="0.9" fill="none"/></svg>
          info@zaviroconstruction.example
        </span>
        <span class="contact-item">
          <svg class="contact-icon" viewBox="0 0 10 10" aria-hidden="true"><circle cx="5" cy="5" r="4.6" fill="var(--orange)"/><path d="M0.6,5 H9.4 M5,0.4 V9.6" stroke="#fff" stroke-width="0.8"/><ellipse cx="5" cy="5" rx="2" ry="4.4" stroke="#fff" stroke-width="0.8" fill="none"/></svg>
          www.zaviroconstruction.example
        </span>
      </div>
    </footer>
  </main>
</body>
</html>
```